Mobile App UI for Telecommunications/Hosting Company

We are about to convert our existing self-service Customer Portal into a mobile phone application and need an elegant and professional UI/UX design. Our company provides telecommunication (voice/mobile/data) and hosting services to medium-sized business. The primary purpose of the application is to view trouble tickets, alerts, orders, and performance charts. This application is available to customers only - not the general public.

Please provide a UI design suitable for display on iPhone/Android devices. The attached document includes a proposed screen flow. You are free to design your own screens to display the same information elegantly.
Updates

Please note that the design should be based on the wireframes in the Word document, not the screenshots.  The screenshots are just to show our existing web portal look & feel.

Also, just a few screens are required for initial submission (3 would be great).

Thanks,
Dermot.

Target Market(s)

IT Managers away from their desk and using a mobile phone application.
Adult males from technical background aged 30-50.
Customers of Brindlewood Networks have access to this application (not the general public). This is a self-service portal for customers only.

Industry/Entity Type

Business

Colors
0592cd
33a6d7
85cae6
cadf82
fde08a

Requirements
Must have
• Please look at the screenshots from our current Customer Portal site (part of the project brief). The mobile app does not have to look the same, but should follow a similar style.

Please check out our company web site at www.brindlewoodnetworks.example (this site is not the customer portal and has a different look at feel) to understand what Brindlewood Networks does.
Nice to have
• Sharing capabilities via email/SMS.
A nice background image to make it stand out
The colours selected below are a guide only as they are similar to the corporate colours
- The priority is something that works on a phone - a design extendable to tablets is a nice to have as our existing web site looks OK on a tablet..

```html
<!DOCTYPE html>
<html lang="en">
<head>
<meta charset="utf-8">
<title>BrindlewoodView – Mobile App Screens</title>
<link rel="stylesheet" href="https://fonts.googleapis.com/css2?family=Source+Sans+3:wght@400;600;700&display=swap">
<style>
:root{
  --page:#eceeef;
  --blue-deep:#0b7fc0;
  --blue:#0592cd;
  --blue-mid:#33a6d7;
  --blue-light:#85cae6;
  --lime:#cadf82;
  --lime-strong:#b9d466;
  --lime-text:#d4e67a;
  --navy:#123f6a;
  --teal:#174a5a;
  --teal-line:#235b6b;
  --orange:#f0866a;
  --ink:#4a4f55;
  --line:#e3e6e8;
  --white:#ffffff;
}
*{box-sizing:border-box;margin:0;padding:0}
html,body{width:1200px;height:715px;overflow:hidden;background:var(--page)}
body{font-family:"Source Sans 3",Arial,sans-serif;position:relative}
h1,h2{font-weight:inherit}
.screen{position:absolute;top:156px;width:228px;height:405px;overflow:hidden;background:linear-gradient(160deg,var(--blue-mid) 0%,var(--blue) 55%,var(--blue-deep) 100%);color:var(--white)}
.screen--login{left:125px}
.screen--user{left:488px}
.screen--menu{left:852px}

.status-bar{position:absolute;left:0;top:0;width:100%;height:15px;background:var(--white);color:#222;font-size:7.5px;display:flex;align-items:center;justify-content:space-between;padding:0 5px;z-index:3}
.status-bar .battery{display:flex;align-items:center;gap:2px}
.status-bar .battery i{display:inline-block;width:13px;height:6px;border:1px solid #333;border-radius:1px;background:linear-gradient(90deg,#333 66%,transparent 66%)}

/* login */
.brand{position:absolute;top:67px;left:0;width:100%;text-align:center}
.brand-name{font-size:14px;font-weight:600;color:var(--navy);letter-spacing:-.2px}
.welcome{position:absolute;top:166px;width:100%;text-align:center;font-size:7px;font-weight:600;color:var(--lime-text);letter-spacing:.2px}
.field{position:absolute;left:23px;width:183px;height:28px;background:var(--white);display:flex;align-items:center;padding-left:8px;gap:7px;font-size:7.5px;color:#9aa3a8}
.field--user{top:188px}
.field--pass{top:227px;letter-spacing:1.5px;color:#888}
.help{position:absolute;top:261px;right:22px;font-size:5.5px;color:var(--lime-text);text-decoration:underline}
.remember{position:absolute;top:278px;left:23px;display:flex;align-items:center;gap:4px;font-size:5.5px;color:var(--lime-text)}
.remember i{width:7px;height:7px;background:var(--lime);display:flex;align-items:center;justify-content:center}
.sign-in{position:absolute;top:303px;left:23px;width:183px;height:22px;background:#0f5e95;display:flex;align-items:center;justify-content:center;gap:4px;font-size:7px;font-weight:700;color:var(--white)}
.sign-in i{width:8px;height:8px;border-radius:50%;background:var(--lime)}
.glow{position:absolute;right:-20px;bottom:-20px;width:140px;height:120px;border-radius:50%;background:radial-gradient(circle,rgba(133,202,230,.55),rgba(133,202,230,0) 70%)}

/* user detail */
.top-nav{position:absolute;top:15px;left:0;width:100%;height:37px;background:var(--lime);display:flex;color:#3a4a2a}
.top-nav .menu-btn{width:65px;display:flex;align-items:center;justify-content:center;border-right:1px solid rgba(255,255,255,.5)}
.top-nav .tab{flex:1;display:flex;flex-direction:column;align-items:center;justify-content:center;font-size:6.5px;gap:2px;border-right:1px solid rgba(255,255,255,.5)}
.top-nav .tab:last-child{border:0;flex:.75}
.title{position:absolute;top:61px;width:100%;text-align:center;font-size:9.5px;font-weight:400;letter-spacing:.3px}
.avatar{position:absolute;border-radius:50%;border:3px solid var(--white);background:radial-gradient(circle at 50% 40%,#c7a98c,#6d5848 70%)}
.screen--user .avatar{top:87px;left:83px;width:62px;height:62px}
.user-name{position:absolute;top:154px;width:100%;text-align:center;font-size:10px}
.edit{position:absolute;top:166px;width:100%;text-align:center;font-size:6px;color:var(--navy);font-weight:600}
.section{position:absolute;left:0;width:100%;font-size:7.5px;font-weight:700;padding-left:13px;display:flex;align-items:center;height:14px;border-bottom:1px solid rgba(255,255,255,.35)}
.section::before{content:"";position:absolute;left:4px;width:5px;height:5px;border-radius:50%;background:#0f3f66}
.settings{position:absolute;top:197px;left:6px;width:216px;height:167px;background:var(--white);border-radius:3px;list-style:none}
.settings li{height:33.4px;display:flex;align-items:center;justify-content:space-between;padding:0 8px;font-size:7.5px;color:var(--ink);border-bottom:1px solid var(--line)}
.settings li:last-child{border:0}
.toggle{width:27px;height:15px;border-radius:8px;background:var(--orange);position:relative;flex:none}
.toggle::after{content:"";position:absolute;top:2px;left:2px;width:11px;height:11px;border-radius:50%;background:var(--white)}
.toggle--on{background:var(--lime-strong)}
.toggle--on::after{left:auto;right:2px}

/* side menu */
.peek{position:absolute;left:201px;top:0;width:27px;height:100%;overflow:hidden}
.peek .top-nav{width:228px;left:0}
.peek .settings{left:0;width:228px}
.drawer{position:absolute;left:0;top:0;width:201px;height:100%;background:var(--teal)}
.screen--menu .avatar{top:39px;left:66px;width:69px;height:69px}
.drawer .user-name{top:124px;font-size:11px;letter-spacing:.4px}
.role{position:absolute;top:139px;width:100%;text-align:center;font-size:7px;font-weight:700;color:var(--lime-text)}
.nav{position:absolute;top:172px;left:0;width:100%;list-style:none;border-top:1px solid var(--teal-line)}
.nav li{height:35.5px;display:flex;align-items:center;gap:11px;padding-left:13px;font-size:8px;border-bottom:1px solid var(--teal-line)}
.nav li svg{width:12px;height:12px;fill:var(--lime-text)}
.nav li.active{background:var(--lime);color:#2f3d22}
.nav li.active svg{fill:#2f3d22}
.power{position:absolute;top:365px;left:89px}
</style>
</head>
<body>

<section class="screen screen--login" aria-label="Sign in screen">
  <div class="status-bar"><span>Tellmo</span><span>9:23 AM</span><span class="battery">66% <i></i></span></div>
  <div class="brand"><span class="brand-name">Brindlewood Networks</span></div>
  <p class="welcome">WELCOME TO BRINDLEWOODVIEW</p>
  <div class="field field--user">
    <svg width="9" height="9" viewBox="0 0 10 10" fill="#b7bfc4"><circle cx="5" cy="3" r="2.4"/><path d="M0.5 10c0-3 2-4.5 4.5-4.5S9.5 7 9.5 10z"/></svg>
    User Name or Email Address
  </div>
  <div class="field field--pass">
    <svg width="9" height="9" viewBox="0 0 10 10" fill="#b7bfc4"><circle cx="5" cy="3" r="2.5"/><rect x="4.2" y="4.5" width="1.6" height="5"/></svg>
    ●●●●●●
  </div>
  <p class="help">Need help logging in?</p>
  <p class="remember"><i><svg width="6" height="6" viewBox="0 0 10 10"><path d="M1 5l3 3 5-6" stroke="#2f3d22" stroke-width="2" fill="none"/></svg></i>Remember my login details</p>
  <div class="sign-in"><i></i>SIGN IN</div>
  <div class="glow"></div>
</section>

<section class="screen screen--user" aria-label="User detail screen">
  <div class="status-bar"><span>Tellmo</span><span>9:23 AM</span><span class="battery">66% <i></i></span></div>
  <nav class="top-nav">
    <div class="menu-btn"><svg width="12" height="9" viewBox="0 0 12 9" fill="#2f3d22"><rect width="12" height="1.6"/><rect y="3.7" width="12" height="1.6"/><rect y="7.4" width="12" height="1.6"/></svg></div>
    <div class="tab"><svg width="8" height="8" viewBox="0 0 10 10" fill="#2f3d22"><path d="M2 0.5l2 2.5-1 1.3c.6 1.3 1.6 2.3 2.9 2.9L7 6l2.5 2-1 1.5C4.5 9.5.5 5.5.5 1.5z"/></svg>Contact &amp; Accounts</div>
    <div class="tab"><svg width="6" height="9" viewBox="0 0 6 10" fill="none" stroke="#2f3d22"><rect x=".5" y=".5" width="5" height="9" rx="1"/></svg>System Access</div>
  </nav>
  <h1 class="title">USER DETAIL</h1>
  <div class="avatar" role="img" aria-label="Profile photo of the signed-in user"></div>
  <p class="user-name">R.Okafor</p>
  <p class="edit">Edit Profile</p>
  <h2 class="section" style="top:182px">HOSTING REPORT AND MANAGEMENT</h2>
  <ul class="settings">
    <li>DNS Management Administrator<span class="toggle toggle--on"></span></li>
    <li>Patching Administrator<span class="toggle"></span></li>
    <li>Access “Restore &amp; Backup” Function<span class="toggle"></span></li>
    <li>Hosting Report<span class="toggle"></span></li>
    <li>View Firewall Configuration<span class="toggle"></span></li>
  </ul>
  <h2 class="section" style="top:368px">TICKETS</h2>
  <h2 class="section" style="top:386px">BILLING</h2>
</section>

<section class="screen screen--menu" aria-label="Side menu screen">
  <div class="peek" aria-hidden="true">
    <div class="top-nav"><div class="menu-btn" style="justify-content:flex-start;padding-left:4px"><svg width="12" height="9" viewBox="0 0 12 9" fill="#2f3d22"><rect width="12" height="1.6"/><rect y="3.7" width="12" height="1.6"/><rect y="7.4" width="12" height="1.6"/></svg></div></div>
    <h2 class="section" style="top:182px">HOSTING</h2>
    <ul class="settings">
      <li>DNS</li><li>Patching</li><li>Access</li><li>Hosting</li><li>View</li>
    </ul>
    <h2 class="section" style="top:368px">TICKETS</h2>
    <h2 class="section" style="top:386px">BILLING</h2>
  </div>
  <div class="drawer">
    <div class="avatar" role="img" aria-label="Profile photo of the signed-in user"></div>
    <p class="user-name">R.Okafor</p>
    <p class="role">Graphic Designer</p>
    <ul class="nav">
      <li><svg viewBox="0 0 12 12"><path d="M0 5.5L12 0 9 12 6 8 10 2 4.5 7z"/></svg>Tickets</li>
      <li><svg viewBox="0 0 12 12"><path d="M11.5.5C7 1 4 4 3 7l2 2c3-1 6-4 6.5-8.5zM2.5 8L0 12l4-2.5z"/></svg>Alerts</li>
      <li class="active"><svg viewBox="0 0 12 12"><path d="M2 1h8v11H2zM4 0h4v2H4z"/></svg>Orders</li>
      <li><svg viewBox="0 0 12 12"><circle cx="6" cy="6" r="4"/><path d="M5 0h2v12H5zM0 5h12v2H0z"/><circle cx="6" cy="6" r="1.6" fill="#174a5a"/></svg>Services</li>
      <li><svg viewBox="0 0 12 12"><path d="M0 2h12v8H0z"/><path d="M0 2l6 4.5L12 2" stroke="#174a5a" fill="none"/></svg>Contact</li>
    </ul>
    <svg class="power" width="22" height="22" viewBox="0 0 22 22" fill="none" stroke="var(--lime)" stroke-width="2.2" stroke-linecap="round"><path d="M6.5 5.5a8 8 0 1 0 9 0"/><path d="M11 2v8"/></svg>
  </div>
</section>

</body>
</html>
```